Stationery Design Project - KLVA Partners

Business Cards
Size: 90mm x 55mm
Letterhead
Size: A4 - 210mm x 297mm
With Compliments Slip
Size: DL - 210mm x 99mm
Presentation Folder
Size: A4

KLVA Partners
website: www.klvapartners.com.au (Under construction)
Offices: *Perth *Brisbane * Seoul

A company that supply Safety consultantcy services

Industry/Entity Type

Business

```html
<!DOCTYPE html>
<html lang="en">
<head>
<meta charset="utf-8">
<title>KLVA Partners – With Compliments Slip</title>
<link rel="stylesheet" href="https://fonts.googleapis.com/css2?family=Michroma&display=swap">
<style>
  :root {
    --page-bg: #e9ebee;
    --paper: #ffffff;
    --ink-navy: #16557f;
    --brand-blue: #1f79bd;
    --band-grey: #bfc1c3;
    --band-blue: #0a78d0;
    --band-sky: #22b5e6;
    --rule: #4a6f86;
    --mist-blue: #dcefff;
    --mist-grey: #eef0f2;
  }
  * { margin: 0; padding: 0; box-sizing: border-box; }
  html, body {
    width: 1200px;
    height: 900px;
    overflow: hidden;
    background: var(--page-bg);
  }
  .slip {
    position: absolute;
    left: 50px;
    top: 190px;
    width: 1100px;
    height: 519px;
    background: var(--paper);
    box-shadow: 0 4px 14px rgba(0,0,0,0.18);
    font-family: "Michroma", sans-serif;
    overflow: hidden;
  }
  .corner-artwork {
    position: absolute;
    right: 0;
    top: 0;
    width: 380px;
    height: 465px;
    background:
      radial-gradient(ellipse at 65% 45%, var(--mist-blue) 0%, var(--mist-grey) 45%, rgba(255,255,255,0) 75%);
  }
  .brand {
    position: absolute;
    left: 80px;
    top: 70px;
    display: flex;
    align-items: center;
    gap: 16px;
  }
  .brand-square {
    width: 44px;
    height: 44px;
    background: var(--band-sky);
  }
  .brand-name {
    font-size: 34px;
    font-weight: 400;
    color: var(--brand-blue);
    letter-spacing: 1px;
  }
  .contact {
    position: absolute;
    left: 715px;
    top: 50px;
    list-style: none;
    color: var(--ink-navy);
    font-size: 14.5px;
    line-height: 21.5px;
    letter-spacing: 1.6px;
    font-variant: small-caps;
    white-space: nowrap;
  }
  .contact .lower { text-transform: lowercase; }
  .rule {
    position: absolute;
    left: 78px;
    top: 417px;
    width: 946px;
    height: 1px;
    background: var(--rule);
  }
  .salutation {
    position: absolute;
    left: 78px;
    top: 428px;
    font-size: 20.5px;
    letter-spacing: 2.6px;
    color: var(--ink-navy);
    font-variant: small-caps;
    white-space: nowrap;
  }
  .footer-band {
    position: absolute;
    left: 0;
    bottom: 0;
    width: 1100px;
    height: 54px;
    background: linear-gradient(to bottom, var(--band-grey) 0%, var(--band-blue) 50%, var(--band-sky) 100%);
  }
</style>
</head>
<body>
  <section class="slip">
    <div class="corner-artwork" role="img" aria-label="Faint decorative artwork in soft white and light blue"></div>

    <div class="brand">
      <span class="brand-square"></span>
      <span class="brand-name">KLVA Partners</span>
    </div>

    <ul class="contact">
      <li>123 Fake Street</li>
      <li>Anytown, New York 12345</li>
      <li>888 888 8888</li>
      <li class="lower">info@klvapartners.com.au</li>
      <li class="lower">www.klvapartners.com.au</li>
    </ul>

    <div class="rule"></div>
    <p class="salutation">With Compliments</p>

    <div class="footer-band" role="img" aria-label="Decorative footer band in grey, blue and sky blue"></div>
  </section>
</body>
</html>
```